Lotven Pharma Chinese Traditional Medicine Web Design

We need a web design for a new company based in Shanghai China called 'Lotven Pharma'. We develop Chinese traditional herbal medicine, including research and development, technical support service, manufacturing, . Also, there’s a small ratio of western medicine. Our goal is to contributing to a healthier future.

Target Market(s)

global,but mainly China

Industry/Entity Type

Pharmaceutical

Number of Pages Required

1 page

Font styles to use
Serif

Colors
e4daeb
cedeed
cadf82
eaf2ce
fbd4d5
fee3d4
fabb94
fee18a
b8a6cd

Requirements
Must have
• triditional Chinese elements, concept of herbal, health, value, better life for people..could be colourful but not more than 3 different colour..
Nice to have
• Style: simple, communicate traditional Chinese herbal medicine element, as well as modern technique..same as LOGO style..
Should not have
• please dont show more IT elements...

```html
<!DOCTYPE html>
<html lang="zh">
<head>
<meta charset="utf-8">
<title>洛文医药（上海）有限公司 · Lotven Pharma</title>
<link rel="stylesheet" href="https://fonts.googleapis.com/css2?family=Noto+Sans+SC:wght@400;500;700&family=Noto+Serif+SC:wght@400;700&display=swap">
<style>
:root{
  --brown:#7a4a30;
  --brown-dark:#5e3722;
  --brown-hero:#8b4a2a;
  --green:#4b5847;
  --grey-bg:#e9eaee;
  --text:#555;
  --text-soft:#777;
  --white:#fff;
}
*{margin:0;padding:0;box-sizing:border-box}
html,body{width:1200px;height:3581px;overflow:hidden}
body{position:relative;background:var(--white);font-family:"Noto Sans SC",sans-serif;color:var(--text)}
.abs{position:absolute}

/* header */
.brand{left:114px;top:14px;width:170px;height:100px;display:flex;align-items:center;gap:10px}
.brand-dot{width:34px;height:34px;border-radius:50%;background:var(--brown);flex:none}
.brand-name{font-family:"Noto Serif SC",serif;font-size:17px;color:var(--brown);line-height:1.2}
.call{left:796px;top:52px;display:flex;align-items:center;gap:6px;color:var(--brown)}
.call small{display:block;font-size:11px;font-weight:700;color:var(--brown-dark);padding-left:30px}
.call b{font-size:13px;color:#444}
.visit{left:1000px;top:44px;text-align:center;font-size:11px;font-weight:700;color:var(--brown-dark)}
.social{display:flex;gap:4px;justify-content:center;margin-top:3px}
.social i{display:block;width:18px;height:18px;border-radius:50%;background:#4a3a30}

.nav{left:0;top:128px;width:1200px;height:39px;background:var(--brown);display:flex;padding-left:117px}
.nav a{display:block;width:163px;text-align:left;padding-left:18px;color:var(--white);text-decoration:none;font-size:22px;line-height:39px}
.nav a.active{background:var(--green);width:133px;margin-right:30px}

/* hero */
.hero{left:0;top:167px;width:1200px;height:535px;overflow:hidden}
.hero-photo{position:absolute;inset:0;background:linear-gradient(100deg,#5b4a3a 0%,#b9b2a5 25%,#e7e4dd 50%,#d8d3c6 68%,#c7b85a 88%,#9fa33a 100%)}
.hero-title{position:absolute;left:0;width:1100px;top:188px;text-align:center;font-size:54px;font-weight:700;line-height:66px;color:var(--brown-hero);-webkit-text-stroke:2px var(--white);paint-order:stroke fill}
.hero-arrow{position:absolute;top:240px}
.dots{position:absolute;left:470px;top:482px;display:flex;gap:14px}
.dots i{width:14px;height:14px;border-radius:50%;background:#c0542c;display:block}
.dots i:first-child{background:var(--white)}

/* section headings */
.heading{left:0;width:1200px;text-align:center;color:#444;font-size:38px;font-weight:500}
.btn{height:42px;width:160px;background:var(--brown);color:var(--white);font-size:19px;font-weight:700;line-height:42px;text-align:center;border-radius:4px;box-shadow:0 2px 3px rgba(0,0,0,.25)}

/* welcome */
.welcome-title{top:790px;font-size:32px;color:var(--brown-dark)}
.rule{left:557px;top:869px;width:116px;height:2px;background:#555}
.intro{left:120px;width:980px;text-align:center;font-size:18px;line-height:20px;color:var(--text)}

/* products */
.products{left:0;top:1186px;width:1200px;height:1017px;background:var(--grey-bg)}
.card{width:297px;height:283px;border:1px solid #999;background:var(--white);padding:4px}
.card div{width:100%;height:100%}
.label{width:297px;text-align:center;font-size:16px;color:#555}

/* newsletter */
.news-band{left:0;top:2203px;width:1200px;height:337px;background:linear-gradient(90deg,#6e3f27,#8a5538 40%,#7a4a30 70%,#5a331f)}
.email-label{left:114px;top:2418px;font-size:32px;color:var(--white)}
.email-input{left:432px;top:2421px;width:455px;height:39px;background:#ebeaed;border:1px solid #ccc}
.email-btn{left:910px;top:2419px;width:170px;height:42px;background:#8d5a3e;color:var(--white);font-size:19px;font-weight:700;line-height:42px;padding-left:16px;border-radius:4px}

/* news */
.news-img{width:259px;height:174px}
.news-cap{width:280px;font-size:14px;color:#555}
.news-date{font-size:12px;color:#777}

/* footer */
.footer{left:0;top:3100px;width:1200px;height:481px}
.foot-brand{left:143px;top:3250px;display:flex;align-items:center;gap:10px}
.foot-brand .brand-dot{background:var(--white)}
.foot-brand .brand-name{color:var(--white);font-size:18px}
.foot-about{left:150px;top:3366px;width:230px;font-size:15px;line-height:20px;color:#f0e6de}
.foot-social{left:176px;top:3470px;display:flex;gap:14px}
.foot-social i{display:block;width:24px;height:24px;border-radius:50%;background:var(--white)}
.col h4{font-size:18px;font-weight:700;color:var(--white);margin-bottom:14px}
.col li{list-style:none;font-size:14px;color:#f3e9e2;line-height:26.5px;padding-left:22px;position:relative}
.col li::before{content:"›";position:absolute;left:2px;font-size:20px;line-height:24px}
.contact p{font-size:14px;color:#f3e9e2;line-height:26.5px;display:flex;align-items:center;gap:8px}
.copy{left:0;top:3520px;width:1200px;height:61px;background:var(--green);text-align:center;color:var(--white);font-size:13px;line-height:61px;font-weight:500}
</style>
</head>
<body>

<header>
  <div class="abs brand"><span class="brand-dot"></span><span class="brand-name">Lotven Pharma<br><small style="font-size:12px">洛文医药</small></span></div>
  <div class="abs call">
    <svg width="26" height="26" viewBox="0 0 24 24"><path fill="#6e3f27" d="M6.6 10.8a15.1 15.1 0 0 0 6.6 6.6l2.2-2.2c.3-.3.7-.4 1-.2 1.1.4 2.3.6 3.6.6.6 0 1 .4 1 1V20c0 .6-.4 1-1 1C10.6 21 3 13.4 3 4c0-.6.4-1 1-1h3.5c.6 0 1 .4 1 1 0 1.3.2 2.5.6 3.6.1.3 0 .7-.2 1z"/></svg>
    <div><small style="padding-left:0">Call Us</small><b>555-210-4477</b></div>
  </div>
  <div class="abs visit">Visit us<div class="social"><i></i><i></i><i></i><i></i></div></div>
  <nav class="abs nav">
    <a class="active">公司首页</a><a>公司概况</a><a>新闻中心</a><a>产品服务</a><a>职业发展</a><a>联系我们</a>
  </nav>
</header>

<section class="abs hero">
  <div class="hero-photo" role="img" aria-label="草药研钵与绿色草药粉的照片"></div>
  <div class="hero-title">個兩把、備我一市有方懷需成沒<br>起動於係本出告會我公卻</div>
  <svg class="hero-arrow" style="left:40px" width="30" height="54" viewBox="0 0 30 54"><path d="M26 4 4 27l22 23" fill="none" stroke="#fff" stroke-width="3"/></svg>
  <svg class="hero-arrow" style="left:1132px" width="30" height="54" viewBox="0 0 30 54"><path d="M4 4l22 23L4 50" fill="none" stroke="#fff" stroke-width="3"/></svg>
  <svg style="position:absolute;left:0;top:0" width="1200" height="535" viewBox="0 0 1200 535">
    <path d="M0 380C150 470 350 505 600 505C820 505 1000 480 1200 440V535H0Z" fill="#7a4a30"/>
    <path d="M0 395C160 490 360 525 600 530C820 532 1000 510 1200 470V535H0Z" fill="#fff"/>
  </svg>
  <div class="dots"><i></i><i></i><i></i><i></i><i></i></div>
</section>

<section>
  <h2 class="abs heading welcome-title">欢迎来到 洛文医药（上海）有限公司</h2>
  <div class="abs rule"></div>
  <p class="abs intro" style="top:912px">洛文医药（上海）有限公司 是一家製藥公司，於2019年在中國上海註冊，致力於研發中草藥，包括研發，技術支持服務，製造以及頂級專家團隊。 而且，西醫的比例很小。</p>
  <p class="abs intro" style="top:972px">中醫的特點是，它不僅可以治癒疾病，而且可以使人們遠離疾病，具有數千年的實踐經驗。 我們的目標是為更健康的未來做出貢獻。</p>
  <div class="abs btn" style="left:510px;top:1070px;width:160px;padding-left:30px">更多信息</div>
</section>

<section class="abs products"></section>
<h2 class="abs heading" style="top:1264px;padding-left:40px">产品服务</h2>
<p class="abs intro" style="top:1358px;left:125px;width:970px;line-height:24px">個兩把、備我一市有方懷需成沒起動於係本出告會我公卻、料高語我語老小，檢再假黑那，就友吃沒足都的價有的，心勢出麼站林以。</p>

<div class="abs card" style="left:134px;top:1451px"><div role="img" aria-label="黑色草药粉与草药精油瓶" style="background:linear-gradient(135deg,#f4eee6,#c79a63 50%,#3a302a)"></div></div>
<div class="abs card" style="left:456px;top:1451px"><div role="img" aria-label="陶碗中的黄绿色草药粉与绿叶" style="background:linear-gradient(135deg,#f6f2ea,#c4b84d 45%,#b5652f 70%,#4e7a34)"></div></div>
<div class="abs card" style="left:777px;top:1451px"><div role="img" aria-label="研钵与多种干草药" style="background:linear-gradient(160deg,#fafafa 40%,#b58e60 70%,#8a3a2a)"></div></div>
<div class="abs label" style="left:134px;top:1744px">产品1</div>
<div class="abs label" style="left:456px;top:1744px">产品2</div>
<div class="abs label" style="left:777px;top:1744px">产品3</div>

<div class="abs card" style="left:134px;top:1792px"><div role="img" aria-label="木研钵、干花与花草茶" style="background:linear-gradient(135deg,#ddd8dc,#8a6a5a 45%,#c9925a 70%,#6b5a7a)"></div></div>
<div class="abs card" style="left:456px;top:1792px"><div role="img" aria-label="木勺中的各式香料" style="background:linear-gradient(135deg,#f3f1ee,#d29b2e 45%,#a3532a 70%,#efe8df)"></div></div>
<div class="abs card" style="left:777px;top:1792px"><div role="img" aria-label="石研钵、草药粉与茶叶" style="background:linear-gradient(135deg,#f5f5f3,#8c9a8a 40%,#c9a27c 70%,#f2eee8)"></div></div>
<div class="abs label" style="left:106px;top:2093px">产品4</div>
<div class="abs label" style="left:428px;top:2093px">产品5</div>
<div class="abs label" style="left:750px;top:2093px">产品6</div>

<section class="abs news-band" role="img" aria-label="干草药与研钵的暗褐色背景照片"></section>
<h2 class="abs heading" style="top:2276px;color:#fff;padding-left:40px">通讯</h2>
<div class="abs email-label">您的电子邮件在这里</div>
<div class="abs email-input"></div>
<div class="abs email-btn">更多信息</div>

<h2 class="abs heading" style="top:2640px;padding-left:40px">新闻中心</h2>
<svg class="abs" style="left:54px;top:2815px" width="28" height="48" viewBox="0 0 28 48"><path d="M24 3 4 24l20 21" fill="none" stroke="#7a4a30" stroke-width="3"/></svg>
<svg class="abs" style="left:1106px;top:2815px" width="28" height="48" viewBox="0 0 28 48"><path d="M4 3l20 21L4 45" fill="none" stroke="#7a4a30" stroke-width="3"/></svg>

<div class="abs news-img" style="left:139px;top:2755px" role="img" aria-label="双手调配草药" background="" ><div style="width:100%;height:100%;background:linear-gradient(135deg,#3d4a2a,#7b5a3a 50%,#c7a27a)"></div></div>
<div class="abs news-img" style="left:460px;top:2755px" role="img" aria-label="实验室工作人员研磨药材"><div style="width:100%;height:100%;background:linear-gradient(135deg,#e8e6e2,#b9b2a8 50%,#6e655a)"></div></div>
<div class="abs news-img" style="left:780px;top:2755px" role="img" aria-label="药房货架上的药罐"><div style="width:100%;height:100%;background:linear-gradient(135deg,#d9dad6,#e6d2a8 50%,#9a8f7c)"></div></div>

<p class="abs news-cap" style="left:139px;top:2954px">備我一市有方懷需成沒起動於係本出告</p>
<p class="abs news-date" style="left:139px;top:2978px">April 26, 2020</p>
<p class="abs news-cap" style="left:460px;top:2954px">料高語我語老小 集修觀快樣理</p>
<p class="abs news-date" style="left:460px;top:2978px">April 29, 2020</p>
<p class="abs news-cap" style="left:780px;top:2954px">用院德我家工廣倒愛得我兒夜力</p>
<p class="abs news-date" style="left:780px;top:2978px">April 30, 2020</p>

<div class="abs btn" style="left:505px;top:3058px;width:160px;padding-left:30px">更多信息</div>

<footer>
  <svg class="abs footer" viewBox="0 0 1200 481" width="1200" height="481">
    <path d="M0 60C220 10 520 0 760 10C940 18 1090 30 1200 40V481H0Z" fill="#4b5847"/>
    <path d="M0 120C260 70 560 55 800 58C980 60 1100 66 1200 72V481H0Z" fill="#fff"/>
    <path d="M0 126C260 78 560 62 800 64C980 66 1100 72 1200 78V481H0Z" fill="#7a4a30"/>
  </svg>
  <div class="abs foot-brand"><span class="brand-dot"></span><span class="brand-name">Lotven Pharma<br><small style="font-size:13px">洛文医药</small></span></div>
  <p class="abs foot-about">洛文医药（上海）有限公司 是一家製藥公司，於2019年在中國上海註冊，致力於研發中草藥，包括研發</p>
  <div class="abs foot-social"><i></i><i></i><i></i></div>

  <div class="abs col" style="left:431px;top:3266px">
    <h4>快速链接</h4>
    <ul><li>公司首页</li><li>新闻中心</li><li>产品服务</li><li>职业发展</li><li>联系我们</li></ul>
  </div>
  <div class="abs col" style="left:587px;top:3266px">
    <h4>其他机构</h4>
    <ul><li>华东产业信息联络中心</li><li>药品质量监管联络处</li><li>中医药事务协调办公室</li><li>医药保健品贸易促进会</li><li>中药产业联合会</li><li>东方草本医学研究所</li><li>药用植物联合研究院</li></ul>
  </div>
  <div class="abs col contact" style="left:884px;top:3266px">
    <h4>联系我们</h4>
    <p><svg width="14" height="14" viewBox="0 0 24 24"><path fill="none" stroke="#fff" stroke-width="2" d="M12 22s7-7 7-12a7 7 0 0 0-14 0c0 5 7 12 7 12z"/><circle cx="12" cy="10" r="2.5" fill="#fff"/></svg>洛文医药（上海）有限公司</p>
    <p style="padding-left:24px">自由贸易试验区青岚路128号</p>
    <p><svg width="14" height="14" viewBox="0 0 24 24"><path fill="none" stroke="#fff" stroke-width="2" d="M6.6 10.8a15 15 0 0 0 6.6 6.6l2.2-2.2 4.6 1.3V20C10.6 21 3 13.4 3 4h3.5l1.3 4.6z"/></svg>555-318-2096</p>
    <p><svg width="14" height="14" viewBox="0 0 24 24"><rect x="3" y="5" width="18" height="14" fill="none" stroke="#fff" stroke-width="2"/><path d="M3 6l9 7 9-7" fill="none" stroke="#fff" stroke-width="2"/></svg>info@lotvenpharma</p>
    <p>沪公网安备 31000000000000号</p>
  </div>
  <div class="abs copy">Copyright@lotvenpharma 2020 All Right Reserved</div>
</footer>

</body>
</html>
```